Business card for dental office with laser therapy / dental facial esthetic

A simple logo which should signifies
Dentistry intraoral as primary and with extended extraoral cosmetic facial esthetic services ( regenerative skincare ) which enhance Beauty as whole .
Conservative high tech approach by using laser intraoral and extraoral limited to face and neck
Front Face :May be black background with neon blue / purplish Rim signifies laser ( ?) & abstract face profile and tooth or Apple design in one ? / see upload inspiration design
Back side : simple appointment slots with date and time / white background / black letter

Color : black/ neon blue/ purplish and gold incorporate for logo design
Final design : dental / esthetic / modern high tech and safe

Target Market(s)

Dental Patients who seeks more high end cosmetic treatment

Industry/Entity Type

Health Care

Contact Information for Business Card

Esthetic modern elegant looking
Logo and office must haves important informations

Logo Text

Family & Cosmetic Dentistry

Font styles to use
Script

Requirements
Must have
• Name of practice and all important informations
• Family & Cosmetic Dentistry
• Lan M. Trieu DMD,PC
• 38472 Orbury Court ,ste.217
• Larkmoor Hills ,VA 20931
• Ph. 555-319-8270
• Fax 555-3195714
Nice to have
• More abstract
• Front : black back ground with neon blue rim (signifies laser therapy)
• Logo can also be golden gold / neon blue
• Address & Infos can be white
Should not have
• Not to busy looking

```html
<!DOCTYPE html>
<html lang="en">
<head>
<meta charset="utf-8">
<title>Lan M. Trieu DMD,PC — Business Card</title>
<link rel="stylesheet" href="https://fonts.googleapis.com/css2?family=Playfair+Display:wght@500;600&family=Barlow+Condensed:wght@500&display=swap">
<style>
  :root {
    --page-bg: #cfcfcf;
    --card-dark: #0a0a0f;
    --card-light: #ffffff;
    --neon-blue: #2fd6ff;
    --neon-purple: #8a5cff;
    --gold: #cfa84f;
    --white: #ffffff;
    --ink: #0a0a0a;
  }
  * { box-sizing: border-box; margin: 0; padding: 0; }
  html, body { width: 1200px; height: 1200px; overflow: hidden; }
  body { background: var(--page-bg); position: relative; }

  .card { position: absolute; left: 192px; width: 821px; height: 470px; overflow: hidden; }
  .card--front {
    top: 29px; background: var(--card-dark);
    border: 2px solid var(--neon-blue);
    box-shadow: inset 0 0 14px rgba(47,214,255,.55), inset 0 0 34px rgba(138,92,255,.35);
  }
  .card--back { top: 578px; background: var(--card-light); }

  .brand-badge {
    position: absolute; left: 584px; top: 42px; width: 198px; height: 198px;
    border-radius: 50%; background: var(--card-dark);
    border: 3px solid var(--neon-blue);
    box-shadow: 0 0 12px var(--neon-blue), 0 0 26px rgba(138,92,255,.7);
    display: flex; flex-direction: column; align-items: center; justify-content: center; text-align: center;
  }
  .brand-name {
    font-family: "Playfair Display", serif; font-weight: 600; font-size: 28px;
    line-height: 1.1; color: var(--gold);
  }
  .brand-tagline {
    margin-top: 8px; font-family: "Playfair Display", serif; font-weight: 500;
    font-size: 13px; line-height: 1.25; letter-spacing: .5px; color: var(--white);
  }

  .practice-name {
    position: absolute; left: 73px; top: 236px;
    font-family: "Playfair Display", serif; font-weight: 500; font-size: 42px; line-height: 1;
    color: var(--gold); white-space: nowrap;
  }

  .contact-list { position: absolute; left: 42px; top: 327px; list-style: none; }
  .contact-item {
    display: flex; align-items: center; height: 31px;
    font-family: "Barlow Condensed", sans-serif; font-weight: 500; font-size: 26px;
    color: var(--white);
  }
  .contact-icon { width: 24px; height: 24px; flex: none; margin-right: 14px; }
  .contact-icon--blank { visibility: hidden; }

  .back-wave { position: absolute; inset: 0; }
  .back-decoration {
    position: absolute; left: 479px; top: 124px; width: 342px; height: 346px;
    background: radial-gradient(ellipse at 55% 50%, rgba(47,214,255,.14) 0%, rgba(138,92,255,.08) 55%, rgba(255,255,255,0) 75%);
  }
  .back-brand { position: absolute; left: 83px; top: 92px; }
  .back-brand__row { display: flex; align-items: center; gap: 12px; }
  .back-brand__dot { width: 26px; height: 26px; border-radius: 50%; background: var(--gold); }
  .back-brand .brand-name { font-size: 32px; color: var(--ink); }
  .back-brand .brand-tagline { margin-top: 6px; margin-left: 38px; font-size: 15px; color: var(--ink); }

  .appointment-title {
    position: absolute; left: 53px; top: 262px;
    font-family: "Playfair Display", serif; font-weight: 600; font-size: 38px; line-height: 1; color: var(--ink);
  }
  .slot { position: absolute; top: 332px; }
  .slot--date { left: 52px; }
  .slot--time { left: 246px; }
  .slot__label {
    font-family: "Playfair Display", serif; font-weight: 500; font-size: 25px;
    color: var(--ink); line-height: 31px;
  }
  .slot__box { width: 177px; height: 60px; background: var(--white); border: 1.5px solid var(--ink); }
</style>
</head>
<body>

<section class="card card--front" aria-label="Card front">
  <div class="brand-badge">
    <span class="brand-name">Trieu<br>Dental</span>
    <span class="brand-tagline">Family &amp; Cosmetic<br>Dentistry</span>
  </div>
  <h1 class="practice-name">LAN M. TRIEU DMD,PC</h1>
  <ul class="contact-list">
    <li class="contact-item">
      <svg class="contact-icon" viewBox="0 0 24 24" aria-hidden="true"><circle cx="12" cy="12" r="12" fill="#fff"/><path d="M12 5a4.5 4.5 0 0 0-4.5 4.5c0 3.3 4.5 9 4.5 9s4.5-5.7 4.5-9A4.5 4.5 0 0 0 12 5z" fill="#0a0a0f"/><circle cx="12" cy="9.5" r="1.7" fill="#fff"/></svg>
      38472 Orbury Court ,ste.217
    </li>
    <li class="contact-item">
      <span class="contact-icon contact-icon--blank"></span>
      Larkmoor Hills ,VA 20931
    </li>
    <li class="contact-item">
      <svg class="contact-icon" viewBox="0 0 24 24" aria-hidden="true"><circle cx="12" cy="12" r="12" fill="#fff"/><path d="M8.3 5.5l2 .2 1 3-1.5 1.2a8 8 0 0 0 4.3 4.3l1.2-1.5 3 1 .2 2c-.3 1.2-1.5 2-2.8 1.8A11 11 0 0 1 6.5 8.3C6.3 7 7.1 5.8 8.3 5.5z" fill="#0a0a0f"/></svg>
      Ph. 555-319-8270
    </li>
    <li class="contact-item">
      <svg class="contact-icon" viewBox="0 0 24 24" aria-hidden="true"><circle cx="12" cy="12" r="12" fill="#fff"/><rect x="8.5" y="5.5" width="7" height="5" fill="none" stroke="#0a0a0f" stroke-width="1.4"/><rect x="6" y="10" width="12" height="6" rx="1" fill="none" stroke="#0a0a0f" stroke-width="1.4"/><rect x="8.5" y="14" width="7" height="4.5" fill="none" stroke="#0a0a0f" stroke-width="1.4"/></svg>
      Fax 555-3195714
    </li>
  </ul>
</section>

<section class="card card--back" aria-label="Card back">
  <svg class="back-wave" viewBox="0 0 821 470" preserveAspectRatio="none" aria-hidden="true">
    <path d="M0 0 C 250 8 430 60 522 143 Q 640 110 760 140 Q 790 128 821 127 V 0 Z" fill="var(--card-dark)"/>
    <path d="M0 0 C 250 8 430 60 522 143 Q 640 110 760 140 Q 790 128 821 127" fill="none" stroke="var(--neon-blue)" stroke-width="3"/>
  </svg>
  <div class="back-decoration" role="img" aria-label="Large faint tooth outline as background decoration"></div>
  <div class="back-brand">
    <div class="back-brand__row"><span class="back-brand__dot"></span><span class="brand-name">Trieu Dental</span></div>
    <div class="brand-tagline">Family &amp; Cosmetic Dentistry</div>
  </div>
  <h2 class="appointment-title">APPOINTMENT</h2>
  <div class="slot slot--date"><div class="slot__label">DATE</div><div class="slot__box"></div></div>
  <div class="slot slot--time"><div class="slot__label">TIME</div><div class="slot__box"></div></div>
</section>

</body>
</html>
```